Quarvine, Cosmetic skin care line

I am not looking to change my logo quarvine on the label just want someone to design a different label I want it to be very classy as it is already just want something different. My product target classier people and people with higher income and for woman and men but mostly women. Looking to keep the label background black

Target Market(s)

Classier and higer income women/men mostly women

Industry/Entity Type

Cosmetics

• I don't really know

Colors

Designer to choose colors to be used in the design.

Requirements
Must have
• It must keep the same quarvine logo and the same matte black background color
Nice to have
• I want a different layout and maybe different fonts for the label
Should not have

```html
<!DOCTYPE html>
<html lang="en">
<head>
<meta charset="UTF-8">
<title>Quarvine – Eye Corrector Serum Labels</title>
<link rel="stylesheet" href="https://fonts.googleapis.com/css2?family=Amatic+SC:wght@700&family=Montserrat:wght@700&display=swap">
<style>
  :root {
    --backdrop: #c4c4c4;
    --matte-black: #353535;
    --gold-deep: #b3952a;
    --gold-light: #dccb6e;
    --gold-line: #c2a534;
    --ink-dark: #2a2a2a;
    --text-light: #f1f1f1;
    --text-soft: #dcdcdc;
  }
  * { margin: 0; padding: 0; box-sizing: border-box; }
  html, body {
    width: 1200px;
    height: 960px;
    overflow: hidden;
    background: var(--backdrop);
  }
  .canvas {
    position: relative;
    width: 1200px;
    height: 960px;
  }

  /* Shared type */
  .brand-name {
    font-family: "Montserrat", sans-serif;
    font-weight: 700;
    color: var(--ink-dark);
    letter-spacing: 0.18em;
    line-height: 1;
    white-space: nowrap;
  }
  .tagline,
  .product-benefit,
  .product-detail {
    font-family: "Amatic SC", cursive;
    font-weight: 700;
    color: var(--text-soft);
    line-height: 1;
    white-space: nowrap;
  }
  .tagline { letter-spacing: 0.16em; }
  .product-benefit { letter-spacing: 0.1em; }
  .product-detail { letter-spacing: 0.08em; }
  .product-type {
    font-family: "Montserrat", sans-serif;
    font-weight: 700;
    color: var(--text-light);
    letter-spacing: 0.14em;
    line-height: 1;
    white-space: nowrap;
  }

  /* Dropper bottle label (portrait, content runs bottom to top) */
  .bottle-label {
    position: absolute;
    left: 224px;
    top: 490px;
    width: 256px;
    height: 330px;
  }
  .bottle-label__body {
    position: absolute;
    left: -37px;
    top: 37px;
    width: 330px;
    height: 256px;
    transform: rotate(-90deg);
    background: var(--matte-black);
    overflow: hidden;
  }
  .bottle-label__band {
    position: absolute;
    left: 0;
    top: 0;
    width: 100%;
    height: 64px;
    background: linear-gradient(90deg, var(--gold-deep), var(--gold-light));
  }
  .bottle-label__brand {
    position: absolute;
    left: 36px;
    top: 15px;
    font-size: 33px;
  }
  .bottle-label__tagline {
    position: absolute;
    left: 116px;
    top: 72px;
    font-size: 22px;
  }
  .bottle-label__type {
    position: absolute;
    left: 50px;
    top: 128px;
    font-size: 48px;
  }
  .bottle-label__rule {
    position: absolute;
    left: 0;
    right: 0;
    top: 188px;
    height: 2px;
    background: var(--gold-line);
  }
  .bottle-label__benefit {
    position: absolute;
    left: 82px;
    top: 200px;
    font-size: 22px;
  }
  .bottle-label__detail {
    position: absolute;
    left: 100px;
    top: 226px;
    font-size: 12px;
  }

  /* Jar label (landscape) */
  .jar-label {
    position: absolute;
    left: 548px;
    top: 556px;
    width: 504px;
    height: 292px;
    background: var(--matte-black);
    overflow: hidden;
  }
  .jar-label__band {
    position: absolute;
    left: 0;
    top: 0;
    width: 100%;
    height: 92px;
    background: linear-gradient(90deg, var(--gold-deep), var(--gold-light));
    display: flex;
    align-items: center;
    justify-content: center;
  }
  .jar-label__brand {
    font-size: 44px;
    padding-left: 0.18em;
  }
  .jar-label__tagline,
  .jar-label__type,
  .jar-label__benefit,
  .jar-label__detail {
    position: absolute;
    left: 0;
    width: 100%;
    text-align: center;
  }
  .jar-label__tagline { top: 104px; font-size: 28px; }
  .jar-label__type { top: 150px; font-size: 62px; }
  .jar-label__rule {
    position: absolute;
    left: 0;
    right: 0;
    top: 220px;
    height: 2px;
    background: var(--gold-line);
  }
  .jar-label__benefit { top: 236px; font-size: 26px; }
  .jar-label__detail { top: 264px; font-size: 15px; }
</style>
</head>
<body>
<main class="canvas">

  <section class="bottle-label" aria-label="Dropper bottle label">
    <div class="bottle-label__body">
      <div class="bottle-label__band"></div>
      <span class="brand-name bottle-label__brand">QUARVINE</span>
      <p class="tagline bottle-label__tagline">FOR ALL</p>
      <h2 class="product-type bottle-label__type">SERUM</h2>
      <div class="bottle-label__rule"></div>
      <p class="product-benefit bottle-label__benefit">EYE CORRECTOR</p>
      <p class="product-detail bottle-label__detail">WITH TRIPLE PEPTIDES</p>
    </div>
  </section>

  <section class="jar-label" aria-label="Jar label">
    <div class="jar-label__band">
      <span class="brand-name jar-label__brand">QUARVINE</span>
    </div>
    <p class="tagline jar-label__tagline">FOR ALL</p>
    <h1 class="product-type jar-label__type">SERUM</h1>
    <div class="jar-label__rule"></div>
    <p class="product-benefit jar-label__benefit">EYE CORRECTOR</p>
    <p class="product-detail jar-label__detail">WITH TRIPLE PEPTIDES</p>
  </section>

</main>
</body>
</html>
```